sommelier *

Sommelier Wine Hospitality Corvanne Star experience I'm working as a sommelier in a Corvanne Star restaurant. I try to reach People who are interested in invest in wine and wine loovers! In terms of color I would like to have a nice color based on a nice bordeaux red (as an advice). By the way i forgot to write my phone number and my email address. 439812604731 kdervin7@postiko.com I hope this info is enough so far.

```html
<!DOCTYPE html>
<html lang="en">
<head>
<meta charset="utf-8">
<title>Dorian Velk – Sommelier business card</title>
<link rel="stylesheet" href="https://fonts.googleapis.com/css2?family=Righteous&family=Kaushan+Script&display=swap">
<style>
  :root {
    --bordeaux: #5e1228;
    --bordeaux-deep: #4a0d1f;
    --bordeaux-soft: #6d1a32;
    --paper: #ffffff;
    --ink: #111111;
    --backdrop: #2a2c30;
  }
  * { box-sizing: border-box; margin: 0; padding: 0; }
  html, body {
    width: 1200px;
    height: 900px;
    overflow: hidden;
    background: var(--backdrop);
  }
  .sheet {
    width: 1200px;
    height: 900px;
    display: flex;
    align-items: center;
    justify-content: center;
    gap: 40px;
  }
  .card {
    position: relative;
    width: 540px;
    height: 310px;
    overflow: hidden;
    border-radius: 4px;
  }
  /* Front */
  .card-front {
    background: radial-gradient(circle at 50% 45%, var(--bordeaux-soft), var(--bordeaux-deep));
  }
  .card-front .texture {
    position: absolute;
    inset: 0;
  }
  .identity {
    position: absolute;
    left: 70px;
    top: 86px;
    color: var(--paper);
  }
  .identity-name {
    font-family: "Righteous", sans-serif;
    font-size: 58px;
    line-height: 1;
    letter-spacing: 1px;
    text-transform: uppercase;
    white-space: nowrap;
  }
  .identity-role {
    font-family: "Kaushan Script", cursive;
    font-size: 28px;
    margin-top: 6px;
  }
  .identity-rule {
    position: absolute;
    left: 190px;
    top: 170px;
    width: 300px;
    height: 10px;
  }
  /* Back */
  .card-back {
    background: var(--paper);
  }
  .contact-band {
    position: absolute;
    left: 60px;
    height: 38px;
    background: var(--bordeaux);
    color: var(--paper);
    font-family: "Righteous", sans-serif;
    font-size: 22px;
    line-height: 38px;
    padding-left: 14px;
    white-space: nowrap;
  }
  .contact-phone { top: 88px; width: 280px; }
  .contact-email { top: 136px; width: 300px; }
  .bottle-art {
    position: absolute;
    left: 360px;
    top: 124px;
    width: 140px;
    height: 64px;
  }
</style>
</head>
<body>
  <main class="sheet">
    <section class="card card-front" aria-label="Card front">
      <svg class="texture" role="img" aria-label="Subtle bordeaux diamond pattern background" width="540" height="310">
        <rect width="540" height="310" fill="var(--bordeaux)" opacity="0.35"/>
      </svg>
      <div class="identity">
        <h1 class="identity-name">Dorian Velk</h1>
        <p class="identity-role">Sommelier</p>
      </div>
      <svg class="identity-rule" width="300" height="10" viewBox="0 0 300 10" aria-hidden="true">
        <rect x="0" y="1" width="300" height="2" fill="var(--paper)"/>
        <rect x="0" y="6" width="300" height="2" fill="var(--paper)"/>
      </svg>
    </section>

    <section class="card card-back" aria-label="Card back">
      <p class="contact-band contact-phone">+43 981 260 4731</p>
      <p class="contact-band contact-email">kdervin7@postiko.com</p>
      <svg class="bottle-art" role="img" aria-label="Wine bottle silhouette lying on its side" width="140" height="64" viewBox="0 0 140 64">
        <rect x="0" y="0" width="140" height="64" rx="10" fill="var(--ink)"/>
      </svg>
    </section>
  </main>
</body>
</html>
```